Flyer Template Design

I have attached 4 files. I would like a design template that could be used across these documents so that they have a common look and feel. The content of the documents is tested and should not be changed significantly. The images can be changed. I have also attache our logo for color compatibility.
Updates

Need extra days to review

Target Market(s)

Wealthy Christian donors

Font styles to use
Serif
Sans Serif

```html
<!DOCTYPE html>
<html lang="en">
<head>
<meta charset="utf-8">
<title>Meridian Outreach – Flyer Series</title>
<link href="https://fonts.googleapis.com/css2?family=Fira+Sans+Condensed:ital,wght@1,500&family=Montserrat:wght@400;700&display=swap" rel="stylesheet">
<style>
:root{
  --page:#e6e6e6;
  --paper:#ffffff;
  --navy:#0d4a7a;
  --title:#1b4d8a;
  --text:#333a40;
  --ink:#1c2b36;
  --green:#43a83a;
  --green-dark:#1e6a2b;
  --rule:#9aa3ab;
}
*{margin:0;padding:0;box-sizing:border-box}
html,body{width:960px;height:1200px;overflow:hidden}
body{background:var(--page);font-family:"Montserrat",sans-serif;color:var(--text);position:relative}
.flyer{position:absolute;width:336px;height:475px;background:var(--paper);overflow:hidden}
.flyer--commission{left:122px;top:105px}
.flyer--nations{left:503px;top:105px}
.flyer--coming{left:313px;top:619px}
.flyer__frame{position:absolute;inset:9px;border:0.6px solid var(--rule);pointer-events:none;z-index:3}
.hero{position:absolute;left:0;top:0;width:336px;height:135px}
.hero--mosque{background:linear-gradient(180deg,#e9eef0 0%,#cfdde0 45%,#1f5f60 80%,#154a4c 100%)}
.hero--hands{background:linear-gradient(135deg,#3a3a3a 0%,#bdbdbd 45%,#7a7a7a 70%,#e0e0e0 100%)}
.hero--field{background:linear-gradient(180deg,#7d8a90 0%,#d8c58c 38%,#f4e6a8 48%,#8c8a4a 60%,#4f6a2a 100%)}
.swoosh{position:absolute;left:0;top:60px;width:336px;height:100px;z-index:1}
.brand{position:absolute;left:22px;top:30px;display:flex;align-items:center;gap:5px;z-index:2}
.brand__mark{width:12px;height:12px;background:var(--green)}
.brand__name{font-family:"Montserrat",sans-serif;font-weight:700;font-size:7px;color:var(--ink);text-transform:uppercase;letter-spacing:0.4px}
.content{position:absolute;left:20px;right:20px;top:150px;bottom:44px;z-index:2}
.title{font-family:"Fira Sans Condensed",sans-serif;font-style:italic;font-weight:500;color:var(--title);text-transform:uppercase;font-size:14px;text-align:center;letter-spacing:-0.2px;margin-bottom:4px}
.subhead{font-family:"Fira Sans Condensed",sans-serif;font-style:italic;font-weight:500;color:var(--title);text-transform:uppercase;font-size:7.4px;margin:6px 0 2px}
.subhead--center{text-align:center}
.callout{font-family:"Fira Sans Condensed",sans-serif;font-style:italic;font-weight:500;color:var(--ink);text-transform:uppercase;font-size:7px;text-align:center;margin:7px 0 3px}
.callout--left{text-align:left;margin-top:0}
p{font-size:4.2px;line-height:1.4;margin-bottom:2px}
.center{text-align:center}
.just{text-align:justify}
strong{font-weight:700}
.split{display:flex;gap:6px;align-items:flex-start}
.split__text{flex:1}
.photo{flex:none;border-radius:2px}
.photo--faces{width:108px;height:90px;background:linear-gradient(135deg,#8a5a3c,#c98a5a 50%,#5a3a2a)}
.photo--faces-tall{width:110px;height:92px;background:linear-gradient(135deg,#6a4030,#c0804e 45%,#3f6a8a 80%)}
.photo--group{width:116px;height:37px;background:linear-gradient(90deg,#3d5e8a,#c9a06a 40%,#8a3c6a 70%,#e9e4d8)}
.photo--sky{width:138px;height:78px;border-radius:6px;background:linear-gradient(180deg,#6f7f88,#e4d497 45%,#6a7a3a 75%,#3f5a22)}
.flyer--commission .content{top:158px}
.flyer--commission .title{margin-bottom:6px}
.flyer--commission .split{margin-top:12px}
.flyer--commission .subhead{margin-top:10px}
.flyer--commission .split .subhead:first-child{margin-top:0}
.flyer--commission .callout{margin:14px 0 6px}
.flyer--commission .subhead--center{margin-top:12px}
.flyer--nations .content{top:158px}
.flyer--nations .title{margin-bottom:8px}
.flyer--nations .subhead{margin-top:12px;margin-bottom:5px}
.flyer--nations .subhead--center{margin-top:14px}
.footer{position:absolute;left:0;right:0;bottom:0;height:40px;background:var(--navy);border-top:2px solid var(--green);color:#fff;text-align:center;padding-top:11px;z-index:2}
.footer p{font-size:4.8px;font-weight:700;margin:0 0 1px}
</style>
</head>
<body>

<article class="flyer flyer--commission">
  <div class="hero hero--mosque" role="img" aria-label="Skyline of domed mosques and minarets under a crescent moon"></div>
  <svg class="swoosh" viewBox="0 0 336 100" preserveAspectRatio="none" aria-hidden="true">
    <path d="M0 20 C90 70 230 70 336 20 L336 100 L0 100 Z" fill="#ffffff"/>
    <path d="M0 18 C90 68 230 68 336 18 L336 24 C230 74 90 74 0 24 Z" fill="var(--green-dark)"/>
    <path d="M0 14 C90 62 230 62 336 8 L336 18 C230 68 90 68 0 18 Z" fill="var(--green)"/>
  </svg>
  <div class="brand"><span class="brand__mark"></span><span class="brand__name">Meridian Outreach</span></div>
  <div class="content">
    <h1 class="title">Finishing the Great Commission</h1>
    <p class="center">Before Jesus ascended into heaven, He commanded his apostles, "Go and make disciples of all nations." For more than 2000 years the church has been working to fulfill this <strong>"Great Commission,"</strong> and much has been accomplished. But now, for the first time in history, our generation has the real opportunity to finish the Great Commission in our lifetimes.</p>
    <div class="split">
      <div class="split__text">
        <h2 class="subhead">It's About Nations</h2>
        <p>In the Bible, the word "nations" refers to people groups: groups of people who share a common ethnicity, culture, and language.</p>
        <p>So when Jesus said, "Go and make disciples of all nations," He was telling us to take the gospel to every people group on earth.</p>
        <p class="just">Amazingly, there are about 12,000 of these people groups scattered throughout the world. And the Great Commission commands us to make disciples in every one of them.</p>
        <h2 class="subhead">Where Do We Stand?</h2>
        <p>Today, there are still about 500 people groups who have never heard the gospel. Most of these groups are small and located in remote, difficult places. These remaining "unengaged" people groups have no known believers.</p>
      </div>
      <div class="photo photo--faces" role="img" aria-label="Grid of portraits of people from many nations"></div>
    </div>
    <p>But now that we know who and where these groups are, by God's grace it is possible that we can engage every one of them with the gospel within the next 3 years.</p>
    <p class="callout">In other words, we can finish the Great Commission!</p>
    <h2 class="subhead subhead--center">Hastening His Coming</h2>
    <p class="center">The Bible says that believers "ought to live holy and godly lives, looking for and hastening the coming of the day of God." It also says that day will not come until the gospel has been preached to "all nations." So how can we hasten the day of his coming? By finishing the work the gave us to do: making disciples in all nations.</p>
    <h2 class="subhead subhead--center">You Can Make That Happen</h2>
    <p class="center">Partner with Meridian Outreach and finance the missionaries who are taking the gospel for the first time to those last remaining people groups. Your investment will <strong>"hasten the coming of the day of God" by accelerating the effort to make "disciples in every nation."</strong> In 2018, our partners helped take the gospel to 231 people groups in 35 countries.</p>
  </div>
  <footer class="footer">
    <p>Join us as we invest to make disciples in "all nations" by 2022</p>
    <p>To learn more, email Daniel Marsh at dmarsh@meridianoutreach.org.</p>
  </footer>
  <div class="flyer__frame"></div>
</article>

<article class="flyer flyer--nations">
  <div class="hero hero--hands" role="img" aria-label="Black and white photo of hands joined together"></div>
  <svg class="swoosh" viewBox="0 0 336 100" preserveAspectRatio="none" aria-hidden="true">
    <path d="M0 40 C90 90 230 90 336 40 L336 100 L0 100 Z" fill="#ffffff"/>
    <path d="M0 38 C90 88 230 88 336 38 L336 44 C230 94 90 94 0 44 Z" fill="var(--green-dark)"/>
    <path d="M0 32 C90 80 230 80 336 28 L336 38 C230 88 90 88 0 38 Z" fill="var(--green)"/>
  </svg>
  <div class="brand"><span class="brand__mark"></span><span class="brand__name">Meridian Outreach</span></div>
  <div class="content">
    <h1 class="title">God Heart the Nation</h1>
    <div class="split">
      <div class="split__text">
        <p>From beginning to end, the Bible reveals God's heart for "the nations."</p>
        <p>In <strong>Genesis</strong>, God promises Abraham, "through your offspring all nations on the earth will be blessed."</p>
        <p>The <strong>Psalms</strong> prophesy that "all the nations you have made will come and worship before you, Lord..."</p>
        <p>In <strong>Isaiah</strong>, God promises the Messiah, "I will make you a light to the nations, that my salvation may reach to the ends of the earth."</p>
        <p>Daniel sees "one like a son of man" who "was given authority, glory and sovereign power; all nations and peoples of every language worshiped him."</p>
        <p>In <strong>Matthew</strong>, Jesus commands his apostles to "Go and make disciples of all nations." And he links his return to the completion of that task, saying, "This gospel of the kingdom will be preached in the whole world as a testimony to all nations, and then the end will come."</p>
      </div>
      <div class="photo photo--faces-tall" role="img" aria-label="Grid of portraits of people in traditional dress"></div>
    </div>
    <p>In <strong>Revelation</strong>, John sees a "great multitude that no one could number, from every nation, from all tribes and peoples and languages, standing before the throne..."</p>
    <p>In the Bible, the word "nations" refers to people groups: groups of people who share a common ethnicity, culture, and language. Amazingly, there are more than 12,000 of these nations scattered around the world—and God has promised that every one of them will be included in His Kingdom.</p>
    <h2 class="subhead">Finishing the Task</h2>
    <div class="split">
      <div class="photo photo--group" role="img" aria-label="Row of women and men from unreached people groups"></div>
      <div class="split__text">
        <p class="just">Today, there are still 500 nations who are not yet represented in God's Kingdom. No one has ever proclaimed the gospel to these "unengaged" people groups, and there are no believers among them. For these groups, God's promises have yet to be fulfilled. Most of these groups are small and located in remote, difficult places.</p>
      </div>
    </div>
    <p>But because we now know who and where they are, by God's grace it is possible that we can engage every one of them with the gospel within the next 3 years.</p>
    <h2 class="subhead subhead--center">You Can Make That Happen</h2>
    <p class="center">Partner with Meridian Outreach and finance the missionaries who are taking the gospel for the first time to those last remaining people groups. Your investment will "hasten the coming of the day of God" by accelerating the effort to make "disciples in every nation." In 2018, our partners helped take the gospel to 231 people groups in 35 countries.</p>
  </div>
  <footer class="footer">
    <p>Join us as we invest to make disciples in "all nations" by 2022</p>
    <p>To learn more, email Daniel Marsh at dmarsh@meridianoutreach.org.</p>
  </footer>
  <div class="flyer__frame"></div>
</article>

<article class="flyer flyer--coming">
  <div class="hero hero--field" role="img" aria-label="Sunrise over a green field beneath a cloudy sky"></div>
  <svg class="swoosh" viewBox="0 0 336 100" preserveAspectRatio="none" aria-hidden="true">
    <path d="M0 40 C90 90 230 90 336 40 L336 100 L0 100 Z" fill="#ffffff"/>
    <path d="M0 38 C90 88 230 88 336 38 L336 44 C230 94 90 94 0 44 Z" fill="var(--green-dark)"/>
    <path d="M0 32 C90 80 230 80 336 28 L336 38 C230 88 90 88 0 38 Z" fill="var(--green)"/>
  </svg>
  <div class="brand"><span class="brand__mark"></span><span class="brand__name">Meridian Outreach</span></div>
  <div class="content">
    <h1 class="title">Hastening His Coming</h1>
    <p class="center">In his second letter, the Apostle Peter asks, what kind of people should believers be? He answers, "We ought to live holy and godly lives, looking for and hastening the coming of the day of God." But how can we do that? How is it possible to hasten the coming of that day?</p>
    <div class="split">
      <div class="split__text">
        <h2 class="subhead">"And Then the End Will Come"</h2>
        <p>When Jesus' disciples asked Him,<br>Tell us, what will be the sign of your coming and of the end of the age?</p>
        <p><strong>He replied,</strong><br>This gospel of the kingdom will be preached in the whole world as a testimony to all nations, and then the end will come.</p>
      </div>
      <div class="photo photo--sky" role="img" aria-label="Sunlit landscape under dramatic clouds"></div>
    </div>
    <h2 class="subhead">When Will Jesus Return?</h2>
    <p class="callout callout--left">He said, only after gospel has been preached to "all nations."</p>
    <p>In the Bible, the word "nations" refers to people groups: groups of people with common ethnicity, culture, and language. Amazingly, there are about 12,000 of these "nations" around the world—and Jesus commanded His church to preach the gospel to all of them!</p>
    <p>Today, there are still 500 people groups without a single believer. No one has ever gone to these remaining "unengaged" groups with the gospel. They do not know the name of Jesus.</p>
    <p class="callout">After 2000 years, isn't it time that they all heard?</p>
    <h2 class="subhead subhead--center">Finishing the Task</h2>
    <p class="center">So how can we "hasten the coming of the day of God?" By completing the work Jesus gave us to do! Jesus said He would not return until the gospel is preached to every nation, so that's what we need to do: take the gospel to all the groups that have never once heard it. Fortunately, we now know who these last groups are and where they are located, by God's grace it is possible that we can engage all of them with the gospel within the next 3 years.</p>
    <h2 class="subhead subhead--center">You Can Make That Happen</h2>
    <p class="center">Partner with Meridian Outreach and finance the missionaries who are taking the gospel for the first time to those last remaining people groups. Your investment will "hasten the coming of the day of God" by accelerating the effort to make "disciples in every nation." In 2018, our partners helped take the gospel to 231 people groups in 35 countries.</p>
  </div>
  <footer class="footer">
    <p>Join us as we invest to make disciples in "all nations" by 2022</p>
    <p>To learn more, email Daniel Marsh at dmarsh@meridianoutreach.org.</p>
  </footer>
  <div class="flyer__frame"></div>
</article>

</body>
</html>
```